captivating, innovative, real estate flyer, double sided

new boutique agency with highly experienced agents,
we have a logo for perch estates logo font in cocogoose. our text font is avenier black, colours are teal 326c charcoal is 426u.
we are all lower case lettering also except for ESTATES all correspondence is lower case also.

what we are looking for:

promoting our services - buy sell rent holiday - market appriasals/whats your property worth, we are located in the stunning jervis bay on south coast of australia postcodes 2540 and 2541.

we will upload the logo for you. either the white or the dark logo we don't mind. (can provide a high res for the dark logo when required)
we would like something a bit different and not comical but entertaining with what we do. we want to be taken seriously but something that clients will remember and possibly something that will stick in their heads. more inclined for a graphical rather than word play

as a promotion.
we would like to offer any clients that list their property for sale with us.
Up to the value of $350.00 either a carpenter pre listing (this is free of charge if they list with us)
an interior designer pre listing for staging of the home
a cleaner pre listing or for a settlement clean

if this could be incorporated on one side only as we are looking for 2 sided brochures.(the promo on one side only)

details that need to be on the brochures are
leonie marsh 0417 862 094 leonie@perchestates.example.com.au
marion pendle 0419/ 537 281 marion@perchestats.example.com.au
office 02 491 72 308 / 1300 48 73 91 info@perchestates.example.com.au

Target Market(s)

all sellers

Industry/Entity Type

Real Estate

Font styles to use
Other font styles liked:
• cocogoose for logo and avenier for text

Colors
00a990
1b1b1b
474747
33b8a4

Requirements
Must have
• light and catchy
Nice to have
• funny but catchy, smart and sophisticated, unusual not the normal for a real estate agency
• teal and charcoal or white it is not a problem if we have either of the logos
Should not have
• pictures of people, comics, the word VALUE is a must not have,

```html
<!DOCTYPE html>
<html lang="en">
<head>
<meta charset="utf-8">
<title>perch estates brochure</title>
<link rel="stylesheet" href="https://fonts.googleapis.com/css2?family=Mulish:wght@400;600;700;800;900&display=swap">
<style>
  :root {
    --teal: #00a990;
    --teal-light: #33b8a4;
    --charcoal: #474747;
    --ink: #1b1b1b;
    --white: #ffffff;
    --backdrop: #a4a4a4;
    --paper: #f4f4f4;
  }
  * { margin: 0; padding: 0; box-sizing: border-box; }
  html, body { width: 1200px; height: 978px; overflow: hidden; background: var(--backdrop); }
  body { font-family: "Mulish", "Helvetica Neue", Arial, sans-serif; }
  .canvas { position: relative; width: 1200px; height: 978px; }

  .page { position: absolute; top: 120px; width: 496px; height: 716px; overflow: hidden; background: var(--paper); }
  .page--back { left: 108px; }
  .page--front { left: 604px; }
  .page__shapes { position: absolute; inset: 0; }

  .brand { position: absolute; text-align: center; color: var(--teal); font-weight: 900; line-height: .9; }
  .brand__name { display: block; letter-spacing: -1px; }
  .brand__tag { display: block; letter-spacing: 1px; }
  .page--back .brand { left: 0; right: 0; top: 48px; }
  .page--back .brand__name { font-size: 62px; }
  .page--back .brand__tag { font-size: 28px; margin-top: 6px; }
  .page--front .brand { left: 0; right: 0; top: 560px; }
  .page--front .brand__name { font-size: 72px; }
  .page--front .brand__tag { font-size: 32px; margin-top: 6px; }

  .why__title { position: absolute; top: 196px; left: 0; right: 0; text-align: center; color: var(--teal); font-size: 25px; font-weight: 700; letter-spacing: 1px; }
  .why__copy { position: absolute; top: 242px; left: 44px; right: 44px; text-align: center; color: var(--white); font-size: 13px; line-height: 1.36; }
  .why__offer { color: var(--teal-light); font-weight: 800; }

  .contact__title { position: absolute; top: 468px; left: 0; right: 0; text-align: center; color: var(--teal); font-size: 33px; font-weight: 700; letter-spacing: .5px; }
  .contact { position: absolute; font-size: 11.5px; color: var(--ink); line-height: 1.45; }
  .contact__name { color: var(--teal); font-size: 14.5px; font-weight: 600; }
  .contact__row { display: flex; align-items: center; gap: 5px; font-weight: 600; }
  .contact__row svg { width: 9px; height: 9px; flex: none; }
  .contact--leonie { left: 32px; top: 528px; }
  .contact--leonie .contact__name { margin-left: 15px; }
  .contact--marion { left: 32px; top: 599px; }
  .contact--marion .contact__name { margin-left: 19px; }
  .contact--office { left: 272px; top: 524px; }
  .contact--office .contact__name { margin-left: 16px; }

  .footer { position: absolute; left: 0; right: 0; bottom: 0; height: 32px; background: var(--teal); border-top: 5px solid var(--charcoal); color: var(--white); font-size: 16px; font-weight: 800; text-align: center; line-height: 27px; }

  .hero { position: absolute; left: 0; top: 0; width: 496px; height: 490px; background: linear-gradient(180deg, #c9d3d8 0%, #9a7f6c 40%, #7d5a48 62%, #5c5350 100%); }
  .banner { position: absolute; left: 0; right: 0; top: 45px; height: 133px; background: rgba(0, 169, 144, .82); color: var(--white); text-align: center; }
  .banner__title { margin-top: 40px; font-size: 35px; font-weight: 700; letter-spacing: .5px; }
  .banner__sub { margin-top: 2px; font-size: 19px; font-weight: 800; }

  .badge { position: absolute; left: 369px; top: 450px; width: 118px; height: 118px; border-radius: 50%; background: var(--white); border: 5px solid var(--teal); color: var(--teal); text-align: center; display: flex; flex-direction: column; justify-content: center; font-weight: 800; line-height: 1.05; }
  .badge__top { font-size: 15px; }
  .badge__main { font-size: 24px; font-weight: 900; }
  .badge__bottom { font-size: 12px; }
</style>
</head>
<body>
<main class="canvas">

  <section class="page page--back">
    <svg class="page__shapes" viewBox="0 0 496 716" preserveAspectRatio="none">
      <rect width="496" height="716" fill="#f4f4f4"/>
      <path d="M0 0 H496 V428 C380 418 250 410 140 430 C80 441 30 452 0 460 Z" fill="#474747"/>
      <path d="M0 460 C30 452 80 441 140 430 C250 410 380 418 496 428 V440 C380 432 240 428 140 446 C80 457 30 472 0 486 Z" fill="#00a990"/>
    </svg>

    <div class="brand"><span class="brand__name">perch</span><span class="brand__tag">ESTATES</span></div>

    <h2 class="why__title">WHY CHOOSE PERCH ESTATES?</h2>
    <p class="why__copy">perch estates is a new boutique agency in stunning Jervis Bay, with highly experienced local agents to help you buy, sell, rent or book a holiday home. Wondering what your property is worth? Ask for a free market appraisal. <span class="why__offer">List your home for sale with us and receive up to $350</span> towards a pre-listing carpenter, an interior designer to stage your home, or a pre-listing or settlement clean.</p>

    <h2 class="contact__title">CONTACT US</h2>

    <div class="contact contact--leonie">
      <div class="contact__name">leonie marsh</div>
      <div class="contact__row"><svg viewBox="0 0 10 10"><circle cx="5" cy="5" r="4.3" fill="none" stroke="#00a990" stroke-width="1"/><path d="M3.4 3.1 L4.2 4.6 C4.7 5.5 5.2 5.9 6.1 6.4 L6.9 5.9" fill="none" stroke="#00a990" stroke-width="1"/></svg>0417 862 094</div>
      <div class="contact__row"><svg viewBox="0 0 10 10"><rect x="1" y="2.5" width="8" height="5.5" fill="#00a990"/><path d="M1 2.5 L5 5.5 L9 2.5" fill="none" stroke="#fff" stroke-width=".8"/></svg>leonie@perchestates.example.com.au</div>
    </div>

    <div class="contact contact--marion">
      <div class="contact__name">marion pendle</div>
      <div class="contact__row"><svg viewBox="0 0 10 10"><circle cx="5" cy="5" r="4.3" fill="none" stroke="#00a990" stroke-width="1"/><path d="M3.4 3.1 L4.2 4.6 C4.7 5.5 5.2 5.9 6.1 6.4 L6.9 5.9" fill="none" stroke="#00a990" stroke-width="1"/></svg>0419/ 537 281</div>
      <div class="contact__row"><svg viewBox="0 0 10 10"><rect x="1" y="2.5" width="8" height="5.5" fill="#00a990"/><path d="M1 2.5 L5 5.5 L9 2.5" fill="none" stroke="#fff" stroke-width=".8"/></svg>marion@perchestats.example.com.au</div>
    </div>

    <div class="contact contact--office">
      <div class="contact__name">office</div>
      <div class="contact__row"><svg viewBox="0 0 10 10"><circle cx="5" cy="5" r="4.3" fill="none" stroke="#00a990" stroke-width="1"/><path d="M3.4 3.1 L4.2 4.6 C4.7 5.5 5.2 5.9 6.1 6.4 L6.9 5.9" fill="none" stroke="#00a990" stroke-width="1"/></svg>02 491 72 308 / 1300 48 73 91</div>
      <div class="contact__row"><svg viewBox="0 0 10 10"><rect x="1" y="2.5" width="8" height="5.5" fill="#00a990"/><path d="M1 2.5 L5 5.5 L9 2.5" fill="none" stroke="#fff" stroke-width=".8"/></svg>info@perchestates.example.com.au</div>
    </div>

    <div class="footer">www.perchestates.example.com.au</div>
  </section>

  <section class="page page--front">
    <div class="hero" role="img" aria-label="Photo of a heritage main street with verandah shopfronts, a cafe and a parked grey SUV"></div>

    <div class="banner">
      <h1 class="banner__title">FIND YOUR DREAM HOME</h1>
      <p class="banner__sub">Jervis Bay’s best properties.</p>
    </div>

    <svg class="page__shapes" viewBox="0 0 496 716" preserveAspectRatio="none">
      <path d="M0 456 C90 468 180 488 260 484 C340 480 420 462 496 440 V716 H0 Z" fill="#474747"/>
      <path d="M0 468 C90 476 180 496 260 494 C340 492 420 470 496 452 V716 H0 Z" fill="#00a990"/>
      <path d="M0 476 C90 486 180 508 260 508 C340 508 420 488 496 472 V716 H0 Z" fill="#f4f4f4"/>
    </svg>

    <div class="badge">
      <span class="badge__top">GENUINE</span>
      <span class="badge__main">LOCAL</span>
      <span class="badge__bottom">EXPERIENCE</span>
    </div>

    <div class="brand"><span class="brand__name">perch</span><span class="brand__tag">ESTATES</span></div>

    <div class="footer">www.perchestates.example.com.au</div>
  </section>

</main>
</body>
</html>
```